We are opening a new restaurant concept called Lanternleaf - Fresh Asian Cuisine. Will be a trendy, casual dining restaurant (somewhat similar to a RJ Wexleys).
I have included pics of our logo in different formats and a picture of our front menu cover and inside menu as well as our actual menu in draft format. Need 6 individual pages total and letter size. Inside cover would be a "about us" type page that describes who we are and mission statement of restaurant (script unwritten at this time), Next page would be appetizers, inside page would have entrees on left and right side of book, then noodles/rice, vegetarian, kids and dessert section, last page would be drink/cocktail menu (still in progress).

```html
<!DOCTYPE html>
<html lang="en">
<head>
<meta charset="utf-8">
<title>Lanternleaf – Appetizers</title>
<link rel="stylesheet" href="https://fonts.googleapis.com/css2?family=Cinzel:wght@700&family=Montserrat:wght@300;600&family=Noto+Serif+SC:wght@700&display=swap">
<style>
  :root {
    --wood-light: #dfe3dc;
    --wood-mid: #c9d3cf;
    --wood-warm: #d8c7b0;
    --paper: #f1f0ee;
    --paper-edge: #e2e1de;
    --title: #6b2e1c;
    --ink: #1f1f1f;
    --ink-soft: #6f6f6f;
    --brush: #222222;
    --lettuce: #8fbf4a;
    --plate: #e9e7e2;
    --pancake: #d9b77e;
    --bowl: #f3f2ef;
    --edamame: #7aa83a;
    --blade: #b9bcbf;
    --handle: #9a6a3c;
  }
  * { box-sizing: border-box; margin: 0; padding: 0; }
  html, body { width: 927px; height: 1200px; overflow: hidden; }
  body { background: var(--wood-light); }

  .menu-page {
    position: relative;
    width: 927px;
    height: 1200px;
    overflow: hidden;
    background: linear-gradient(135deg, var(--wood-light) 0%, var(--wood-mid) 45%, var(--wood-warm) 100%);
  }

  .food-photo { position: absolute; }
  .lettuce-wraps {
    left: 0; top: 18px; width: 310px; height: 265px;
    border-radius: 18px;
    background: radial-gradient(ellipse at 50% 50%, #b6d86a 0%, var(--lettuce) 55%, #3a3a38 100%);
  }
  .scallion-pancakes {
    left: 630px; top: 30px; width: 330px; height: 360px;
    border-radius: 50%;
    background: radial-gradient(circle at 45% 55%, var(--pancake) 0%, #e8d2a5 50%, var(--plate) 72%);
  }
  .edamame-bowl {
    left: 660px; top: 868px; width: 300px; height: 300px;
    border-radius: 50%;
    background: radial-gradient(circle at 50% 50%, var(--edamame) 0%, #c8a36a 45%, var(--bowl) 66%);
  }
  .chef-knife {
    left: -20px; top: 890px; width: 420px; height: 330px;
    background: linear-gradient(140deg, var(--handle) 0%, var(--handle) 22%, var(--blade) 24%, #d7d9db 70%, transparent 71%);
    clip-path: polygon(0 10%, 20% 0, 100% 95%, 90% 100%, 0 40%);
  }

  .menu-sheet {
    position: absolute;
    left: 62px; top: 250px;
    width: 745px; height: 830px;
    background: radial-gradient(ellipse at 50% 40%, var(--paper) 0%, var(--paper-edge) 100%);
    border-radius: 22px;
    transform: rotate(-4deg);
    box-shadow: 0 3px 10px rgba(0,0,0,0.18);
  }

  .section-heading { position: absolute; left: 0; right: 0; top: 38px; text-align: center; }
  .section-heading .chinese {
    font-family: "Noto Serif SC", serif; font-weight: 700;
    font-size: 17px; color: var(--ink); letter-spacing: 2px;
  }
  .section-heading .title {
    font-family: "Cinzel", serif; font-weight: 700;
    font-size: 46px; color: var(--title); line-height: 1; margin-top: 2px;
  }
  .section-heading .brush {
    display: block; margin: 2px auto 0; width: 300px; height: 12px;
  }

  .menu-column {
    position: absolute; top: 155px; width: 300px;
    display: flex; flex-direction: column;
    font-family: "Montserrat", sans-serif;
  }
  .menu-column.left { left: 95px; gap: 15px; }
  .menu-column.right { left: 420px; top: 128px; gap: 15px; }

  .dish-name { font-weight: 600; font-size: 16px; color: var(--ink); line-height: 17px; }
  .dish-desc { font-weight: 300; font-size: 15px; color: var(--ink-soft); line-height: 15px; }
</style>
</head>
<body>
<main class="menu-page">
  <div class="food-photo lettuce-wraps" role="img" aria-label="Lettuce wraps with ground chicken and pickled vegetables on a dark plate"></div>
  <div class="food-photo scallion-pancakes" role="img" aria-label="Scallion pancake wedges with dipping sauce and chopsticks"></div>
  <div class="food-photo chef-knife" role="img" aria-label="Chef knife with wooden handle"></div>
  <div class="food-photo edamame-bowl" role="img" aria-label="Bowl of rice with chicken, edamame and peppers with chopsticks"></div>

  <section class="menu-sheet">
    <header class="section-heading">
      <div class="chinese">开胃菜</div>
      <h1 class="title">APPETIZERS</h1>
      <svg class="brush" viewBox="0 0 300 12" aria-hidden="true">
        <path d="M2 7 Q80 2 298 3 L296 9 Q120 11 6 11 Z" fill="var(--brush)"/>
      </svg>
    </header>

    <div class="menu-column left">
      <div class="dish"><div class="dish-name">Edamame $4</div><div class="dish-desc">Seasoned &amp; boiled soy bean</div></div>
      <div class="dish"><div class="dish-name">Scallion Pancakes $6</div><div class="dish-desc">Traditional Chinese flatbread folded with oil and minced scallions and pan fried</div></div>
      <div class="dish"><div class="dish-name">Lanternleaf Lettuce Wraps $8</div><div class="dish-desc">Seasoned ground chicken wrapped in lettuce and drizzled with our secret sauce</div></div>
      <div class="dish"><div class="dish-name">Salt &amp; Pepper Calamari $9</div><div class="dish-desc">Crispy Calamari with Green &amp; red peppers and onions</div></div>
      <div class="dish"><div class="dish-name">Singapore Ribs $9</div><div class="dish-desc">Tender baby back ribs in a sweet homemade glaze</div></div>
      <div class="dish"><div class="dish-name">Spicy Bang Bang Shrimp $9</div><div class="dish-desc">Crispy fried shrimp tossed in our creamy spicy sauce</div></div>
      <div class="dish"><div class="dish-name">Drunken Chicken $8</div><div class="dish-desc">Chicken, Thai chili and a house made spicy sauce</div></div>
      <div class="dish"><div class="dish-name">Sichuan Spiced Beef $9</div><div class="dish-desc">Beef Shank, beef tripe, cilantro, peanuts and celery</div></div>
      <div class="dish"><div class="dish-name">Beef Crispy Bottom Bow $10</div><div class="dish-desc">Pan fried crispy bottom Bao, stuffed with beef, drizzled with scallion and sesame</div></div>
      <div class="dish"><div class="dish-name">Crispy Mala Beef Jerky $9</div><div class="dish-desc">Dry fried shredded beef with fresh celery, Serrano peppers, garlic, green onion in soy sauce and peppercorn oil</div></div>
    </div>

    <div class="menu-column right">
      <div class="dish"><div class="dish-name">Steamed Chicken Dumplings (6) $6</div><div class="dish-desc">Chinese dumpling stuffed with Chicken, Shiitake mushrooms and bamboo shoots</div></div>
      <div class="dish"><div class="dish-name">Red Oil Dumplings (6) $7</div><div class="dish-desc">Pork filled dumplings in Sichuan red oil sauce drizzled with sesame</div></div>
      <div class="dish"><div class="dish-name">Pork Egg Rolls (2) $4</div><div class="dish-desc">Hand rolled with julienned veggies with our sweet n' sour mustard sauce</div></div>
      <div class="dish"><div class="dish-name">Vegetarian Spring Rolls (3) $4</div><div class="dish-desc">Fresh rice paper roll filled with vermicelli, bean sprouts and lettuce. Served with peanut sauce</div></div>
      <div class="dish"><div class="dish-name">Garlic Cucumber Salad $7</div><div class="dish-desc">Sliced cucumber with a garlic vinaigrette</div></div>
      <div class="dish"><div class="dish-name">Lanternleaf Hot n' Sour Soup $4</div><div class="dish-desc">Tangy broth with Bamboo shoot, wood ear fungus, tofu, egg and carrots</div></div>
      <div class="dish"><div class="dish-name">West Lake Soup $4</div><div class="dish-desc">Light creamy soup with ground beef, diced Shiitake mushroom, tofu, bamboo shoots, egg white and cilantro</div></div>
    </div>
  </section>
</main>
</body>
</html>
```